GHollis Busisness Card

I am an aerospace consultant and at this time only need business cards.

Industry/Entity Type

Business

Contact Information for Business Card

Hollis Partners,LLC
Gerald T. Hollis

348 Birch Hollow Road
Madison AL 35762

256-555-0148 (cell)
256-555-0173 (fax)

geraldhollis@mailbrook.net

```html
<!DOCTYPE html>
<html lang="en">
<head>
<meta charset="utf-8">
<title>Hollis Partners, LLC – Business Card</title>
<link href="https://fonts.googleapis.com/css2?family=Bebas+Neue&family=Source+Sans+3:wght@400;700&display=swap" rel="stylesheet">
<style>
  :root {
    --backdrop: #4b4b4b;
    --card: #f6f8f8;
    --brand-blue: #115f9e;
    --ink: #111111;
  }
  * { margin: 0; padding: 0; box-sizing: border-box; }
  html, body {
    width: 1200px;
    height: 999px;
    overflow: hidden;
    background: var(--backdrop);
  }
  .business-card {
    position: absolute;
    left: 75px;
    top: 199px;
    width: 1050px;
    height: 600px;
    background: var(--card);
    overflow: hidden;
  }
  .company-name {
    position: absolute;
    left: 51px;
    top: 70px;
    font-family: "Bebas Neue", "Oswald", sans-serif;
    font-size: 80px;
    line-height: 1;
    color: var(--brand-blue);
    letter-spacing: 0.5px;
    white-space: nowrap;
  }
  .address-block {
    position: absolute;
    left: 51px;
    top: 274px;
    font-family: "Source Sans 3", "Myriad Pro", sans-serif;
    font-size: 27px;
    line-height: 35px;
    color: var(--ink);
  }
  .address-block .person-name { font-weight: 700; }
  .contact-list {
    position: absolute;
    left: 51px;
    top: 404px;
    list-style: none;
    font-family: "Source Sans 3", "Myriad Pro", sans-serif;
    font-size: 27px;
    color: var(--ink);
  }
  .contact-item {
    display: flex;
    align-items: center;
    height: 42px;
  }
  .contact-icon {
    width: 32px;
    height: 32px;
    margin-right: 12px;
    flex: none;
  }
  .footer-band {
    position: absolute;
    top: 549px;
    height: 51px;
    background: var(--brand-blue);
  }
  .footer-band.main { left: 0; width: 748px; }
  .footer-band.block-1 { left: 772px; width: 60px; }
  .footer-band.block-2 { left: 848px; width: 60px; }
  .footer-band.block-3 { left: 924px; width: 59px; }
</style>
</head>
<body>
  <main class="business-card">
    <h1 class="company-name">Hollis Partners, LLC</h1>

    <div class="address-block">
      <div class="person-name">Gerald T.</div>
      <div>Hollis 348 Birch Hollow</div>
      <div>Road Madison AL</div>
    </div>

    <ul class="contact-list">
      <li class="contact-item">
        <svg class="contact-icon" viewBox="0 0 32 32" aria-hidden="true">
          <rect x="1" y="1" width="30" height="30" rx="5" fill="var(--brand-blue)"/>
          <path d="M11 7c1.5-.8 2.5 0 3 1l1.5 3.5c.4 1-.2 1.7-1 2.2-.6.4-.6 1 0 2.4l2 3.4c.8 1.3 1.3 1.5 2 1.2.9-.4 1.8-.6 2.4.3l2 3c.6.9.2 1.8-.8 2.5-2.5 1.6-5.5.3-8.5-4.8S8.5 8.6 11 7z" fill="#fff"/>
        </svg>
        <span>35762 256-555-0148</span>
      </li>
      <li class="contact-item">
        <svg class="contact-icon" viewBox="0 0 32 32" aria-hidden="true">
          <rect x="9" y="1" width="14" height="14" fill="var(--brand-blue)"/>
          <rect x="11" y="4" width="10" height="1.5" fill="#fff"/>
          <rect x="11" y="7.5" width="10" height="1.5" fill="#fff"/>
          <rect x="11" y="11" width="10" height="1.5" fill="#fff"/>
          <rect x="1" y="16" width="30" height="15" rx="2" fill="var(--brand-blue)"/>
          <path d="M9 25c0-3 14-3 14 0v1.5h-3.5v-1.8c-2-.7-5-.7-7 0v1.8H9z" fill="#fff"/>
        </svg>
        <span>256-555-0173</span>
      </li>
      <li class="contact-item">
        <svg class="contact-icon" viewBox="0 0 32 32" aria-hidden="true">
          <path d="M1 13 16 3l15 10v17H1z" fill="var(--brand-blue)"/>
          <path d="M6 13h20v6l-10 6-10-6z" fill="#fff"/>
          <path d="M1 13l15 10 15-10" fill="none" stroke="var(--brand-blue)" stroke-width="2"/>
          <circle cx="16" cy="17" r="2.5" fill="var(--brand-blue)"/>
        </svg>
        <span>geraldhollis@mailbrook.net</span>
      </li>
    </ul>

    <div class="footer-band main"></div>
    <div class="footer-band block-1"></div>
    <div class="footer-band block-2"></div>
    <div class="footer-band block-3"></div>
  </main>
</body>
</html>
```